Product label for herbal salves, lotions, soaps and tinctures

We need a very simple, clean and organic looking label that can be used for an ointment jar, a lotion bottle and a dropper bottle.
We have an existing logo (see attached). We like the colors white, olive green, gold and black. It needs to include product name as dominant and logo. It also needs to include an ingredient list, and usage statement. Include weight of product, distributed by, made in the USA, and NQB statement.
Example of what needs to be present:
Logo
Name: Calmwick Balm
Used for: For Muscle Aches, Arthritis, Tendonitis, Headaches
To Use: For muscle aches, arthritis and tendonitis, massage into affected area. For tension headache apply to neck, temples and forehead.
Store in a cool and dry place, away from direct heat and sunlight.
Weight of product: 1.75
DIST. BY: Brookmere Herbal
Made in the USA
This product is not intended to diagnose, treat, cure
or prevent any disease. Not regulated
by the NQB. Please consult your health care practitioner
before using product. Discontinue use if any adverse reaction occurs.
Ingredient list:
Wildcrafted Ingredients:
Ashwagandha Root, Peppermint Leaf, Hops Flowers, St. John’s Wort Herb, Arnica Flowers, Green Tea Leaf, Alfalfa Leaf, Dandelion Root, Burdock Root, Chickweed Herb, Chaparral Leaf, Yarrow Flowers, Boneset Herb, Moringa Leaf, Meadowsweet Herb, Nettle Leaf
Organic Ingredients:
Olive Oil, Aloe Leaf, Sweet Birch Bark, Helichrysum Flowers, Holy Basil Leaf, Borage Herb, Ginger Root, Angelica Root, White Willow Bark, Mustard Seed, Beeswax, Vitamin E, Essential Oils
Dimensions of Jar:
Circumference: 7 in.
Height: 1 in.

```html
<!DOCTYPE html>
<html lang="en">
<head>
<meta charset="utf-8">
<title>Brookmere Herbal – Calmwick Balm Label</title>
<link rel="stylesheet" href="https://fonts.googleapis.com/css2?family=Quicksand:wght@400;500;700&family=Hind:wght@400;500&display=swap">
<style>
  :root {
    --olive: #6b702c;
    --olive-dark: #5b5f24;
    --gold: #c98f2a;
    --ink: #555555;
    --white: #ffffff;
    --backdrop: #f3f3ef;
    --sprig: #d9d9d6;
  }
  * { margin: 0; padding: 0; box-sizing: border-box; }
  html, body {
    width: 1200px; height: 810px; overflow: hidden;
    background: var(--backdrop);
    font-family: "Hind", sans-serif;
  }
  .label-sheet {
    position: absolute; left: 26px; top: 322px;
    width: 1148px; height: 166px;
    display: flex; gap: 12px;
  }
  .panel {
    flex: 1; height: 100%;
    position: relative;
  }
  .panel--text {
    background: var(--olive);
    color: var(--white);
    text-align: center;
    padding: 14px 18px;
  }
  .usage {
    font-size: 9.6px; font-weight: 500; line-height: 1.55;
    margin-bottom: 12px;
  }
  .fine-print {
    font-size: 7.4px; line-height: 1.95;
  }
  .fine-print .gap { display: inline-block; width: 22px; }
  .panel--front {
    background: var(--white);
    text-align: center;
  }
  .sprig {
    position: absolute; top: 0; width: 120px; height: 70px;
    background: radial-gradient(ellipse at center, var(--sprig) 0%, rgba(217,217,214,0) 70%);
    opacity: .8;
  }
  .sprig--left { left: 0; }
  .sprig--right { right: 0; }
  .brand {
    position: absolute; top: 38px; left: 0; right: 0;
    display: flex; align-items: center; justify-content: center; gap: 6px;
    font-family: "Quicksand", sans-serif; font-weight: 700;
    font-size: 22px; color: var(--olive);
  }
  .brand-dot {
    width: 9px; height: 9px; border-radius: 50%; background: var(--olive);
  }
  .product-name {
    position: absolute; top: 100px; left: 0; right: 0;
    font-family: "Quicksand", sans-serif; font-weight: 400;
    font-size: 26px; color: var(--ink); letter-spacing: .5px;
  }
  .rule {
    position: absolute; top: 138px; left: 50%; transform: translateX(-50%);
    width: 228px; height: 1px; background: var(--gold);
  }
  .uses {
    position: absolute; top: 142px; left: 0; right: 0;
    font-family: "Quicksand", sans-serif; font-weight: 500;
    font-size: 8.2px; color: var(--olive-dark); letter-spacing: .3px;
  }
  .ingredients {
    font-size: 7.6px; line-height: 1.98; padding-top: 14px;
  }
</style>
</head>
<body>
  <main class="label-sheet">
    <section class="panel panel--text">
      <p class="usage">For muscle aches, arthritis and tendonitis, massage into affected area.<br>For tension headache apply to neck, temples and forehead.</p>
      <p class="fine-print">
        Store in a cool and dry place, away from direct heat and sunlight.<br>
        Weight of product: 1.75<span class="gap"></span>DIST. BY: Brookmere Herbal<br>
        MADE IN THE USA<br>
        This product is not intended to diagnose, treat, cure or prevent any disease.<br>
        Not regulated by the NQB. Please consult your health care practitioner<br>
        before using product. Discontinue use if any adverse reaction occurs.
      </p>
    </section>

    <section class="panel panel--front">
      <div class="sprig sprig--left" role="img" aria-label="Faint line drawing of an olive sprig"></div>
      <div class="sprig sprig--right" role="img" aria-label="Faint line drawing of an olive sprig"></div>
      <div class="brand"><span class="brand-dot"></span>Brookmere Herbal</div>
      <h1 class="product-name">Calmwick Balm</h1>
      <div class="rule"></div>
      <p class="uses">For Muscle Aches, Arthritis, Tendonitis, Headaches</p>
    </section>

    <section class="panel panel--text">
      <p class="ingredients">
        Ingredient list:<br>
        Wildcrafted Ingredients:<br>
        Ashwagandha Root, Peppermint Leaf, Hops Flowers, St. John’s Wort Herb, Arnica Flowers, Green Tea Leaf, Alfalfa Leaf, Dandelion Root, Burdock Root, Chickweed Herb, Chaparral Leaf, Yarrow Flowers, Boneset Herb, Moringa Leaf, Meadowsweet Herb, Nettle Leaf<br>
        Organic Ingredients:<br>
        Olive Oil, Aloe Leaf, Sweet Birch Bark, Helichrysum Flowers, Holy Basil Leaf, Borage Herb, Ginger Root, Angelica Root, White Willow Bark, Mustard Seed, Beeswax, Vitamin E, Essential Oils
      </p>
    </section>
  </main>
</body>
</html>
```